Webbanner-Design für Verkäufer von versilberten Wohnaccessoires
Zielgruppe
Wir verkaufen versilberte Wohnaccessoires (Luxus)
www.morvani-casa.de
Aufgabenstellung
Wir sind auf der Suche nach drie Bannern die bei uns auf der Webseite durchlaufen (www.morvani-casa.de)
1. Banner:
Schriftzug: Deko-Highlights für das perfekte Dinner
3x Buttons: GLÄSER / LEUCHTER / KARAFFEN
2. Banner: Die Teelichterkerze - Entdecke die genial Idee
2x Buttons: Kerze mit Ø 8cm / Kerze mit Ø 10cm
3. Banner: Die gemütlichste Dekoration zu Weihnachten
3x Buttons: Teelichter / Adventskränze / Dekoration
4. Banner: Glänzende Bilderrahmen - das perfekte Geschenk!
3x Buttons: 10x15cm / 13x18cm / 15x20cm

```html
<!DOCTYPE html>
<html lang="de">
<head>
<meta charset="utf-8">
<title>Morvani – Versilberte Wohnaccessoires</title>
<link rel="stylesheet" href="https://fonts.googleapis.com/css2?family=Montserrat:wght@300;400;500;600&family=Open+Sans:wght@400;600;700&display=swap">
<style>
:root{
  --ink:#111;
  --text:#222;
  --white:#fff;
  --bar:#0d0d0d;
  --btn-light:#e6e6e6;
  --btn-dark:#151515;
  --cart-bg:#e4e4e4;
  --tile-border:#d6d6d6;
}
*{margin:0;padding:0;box-sizing:border-box}
html,body{width:1200px;height:607px;overflow:hidden;background:var(--white)}
body{font-family:"Open Sans",Arial,sans-serif;color:var(--text);position:relative}
.cookie-notice{position:absolute;left:0;top:0;width:1200px;height:46px;border-top:1px solid #ddd}
.cookie-notice p{position:absolute;left:162px;top:16px;font-size:10px}
.cookie-accept{position:absolute;left:955px;top:8px;width:89px;height:30px;background:var(--ink);color:var(--white);font-size:10px;font-weight:700;display:flex;align-items:center;justify-content:center;border-right:2px solid #555}
.brand{position:absolute;left:161px;top:62px;width:110px;height:42px;display:flex;align-items:center;justify-content:center;font-family:"Montserrat",sans-serif;font-weight:500;font-size:22px;letter-spacing:1px;color:var(--ink)}
.utility-nav span{position:absolute;top:53px;display:flex;align-items:center;gap:4px;font-size:10px;white-space:nowrap}
.cart{position:absolute;left:943px;top:46px;width:93px;height:27px;background:var(--cart-bg);font-size:10px;font-weight:600;display:flex;align-items:center;justify-content:center;gap:6px}
.main-nav{position:absolute;top:88px;right:170px;display:flex;gap:10px;font-size:12px;align-items:center;color:var(--ink);white-space:nowrap}
.usp-bar{position:absolute;left:0;top:118px;width:1200px;height:27px;background:var(--bar);color:var(--white);font-size:9.5px}
.usp-bar span{position:absolute;top:7px;display:flex;align-items:center;gap:7px;white-space:nowrap}
.hero{position:absolute;left:161px;top:145px;width:875px;height:321px;overflow:hidden;background:#3b3739}
.hero-visual{position:absolute;inset:0;background:
  radial-gradient(ellipse 14% 10% at 40% 12%,rgba(255,200,120,.55),rgba(255,200,120,0)),
  radial-gradient(ellipse 14% 10% at 59% 10%,rgba(255,200,120,.55),rgba(255,200,120,0)),
  radial-gradient(ellipse 48% 38% at 50% 88%,rgba(190,190,195,.55),rgba(120,120,125,0)),
  linear-gradient(90deg,#b9b9bc 0%,#8c8a8d 20%,#2a2530 30%,#1f1a26 50%,#2a2530 70%,#8e8985 82%,#d8cfbf 100%)}
.hero-title{position:absolute;left:0;width:100%;text-align:center;color:var(--white);font-family:"Montserrat",sans-serif;font-weight:300}
.hero-title.main{top:112px;font-size:40px}
.hero-title.sub{top:161px;font-size:25px}
.hero-cta{position:absolute;top:220px;height:40px;display:flex;font-family:"Montserrat",sans-serif;font-size:13.5px;font-weight:500}
.hero-cta .label{width:162px;background:var(--btn-light);color:var(--ink);display:flex;align-items:center;justify-content:center}
.hero-cta .arrow{width:41px;background:var(--btn-dark);display:flex;align-items:center;justify-content:center}
.tile{position:absolute;top:481px;width:208px;height:130px;border:1px solid var(--tile-border)}
</style>
</head>
<body>
<div class="cookie-notice">
  <p>Diese Website verwendet Cookies, um Ihnen die bestmögliche Funktionalität bieten zu können.</p>
  <div class="cookie-accept">Einverstanden</div>
</div>

<div class="brand">MORVANI</div>

<div class="utility-nav">
  <span style="left:698px"><svg width="10" height="10" viewBox="0 0 10 10"><circle cx="4" cy="4" r="3" fill="none" stroke="#111" stroke-width="1.5"/><line x1="6.2" y1="6.2" x2="9.3" y2="9.3" stroke="#111" stroke-width="1.6"/></svg>Suchen</span>
  <span style="left:766px">Service/Hilfe <svg width="9" height="6" viewBox="0 0 9 6"><path d="M1 1l3.5 3.5L8 1" fill="none" stroke="#111" stroke-width="1.4"/></svg></span>
  <span style="left:857px">Mein Konto <svg width="9" height="6" viewBox="0 0 9 6"><path d="M1 1l3.5 3.5L8 1" fill="none" stroke="#111" stroke-width="1.4"/></svg></span>
</div>
<div class="cart"><svg width="12" height="11" viewBox="0 0 12 11"><path d="M0 1h2l1.5 6h7L12 3H3" fill="none" stroke="#111" stroke-width="1.4"/><circle cx="4.5" cy="9.5" r="1" fill="#111"/><circle cx="9.5" cy="9.5" r="1" fill="#111"/></svg>Warenkorb</div>

<nav class="main-nav">
  <svg width="12" height="11" viewBox="0 0 12 11"><path d="M6 0L0 5.5h1.7V11h3V7.5h2.6V11h3V5.5H12z" fill="#111"/></svg>
  <span>Geschenke</span><span>NEU</span><span>Material</span><span>Bar</span><span>Tafel</span><span>Wohnen</span><span>Accessoires</span><span>Kinder</span><span>Sorvu Porzellan</span><span>Weihnachten</span><span>SALE</span>
</nav>

<div class="usp-bar">
  <span style="left:160px"><svg width="12" height="9" viewBox="0 0 12 9"><rect x="0" y="1" width="7" height="5" fill="#fff"/><path d="M7 3h3l2 2v1H7z" fill="#fff"/><circle cx="2.5" cy="7" r="1.3" fill="#fff"/><circle cx="9.5" cy="7" r="1.3" fill="#fff"/></svg>Kostenloser Versand ab € 20,- Bestellwert</span>
  <span style="left:454px"><svg width="11" height="11" viewBox="0 0 11 11"><circle cx="5.5" cy="5.5" r="4.5" fill="none" stroke="#fff" stroke-width="1.3"/><path d="M5.5 3v2.8l2 1.2" fill="none" stroke="#fff" stroke-width="1.2"/></svg>Versand innerhalb von 48h*</span>
  <span style="left:662px"><svg width="10" height="10" viewBox="0 0 10 10"><rect x="0" y="4" width="2" height="6" fill="#fff"/><path d="M3 4l2-4c1 0 1.4.7 1.2 1.6L6 4h3.2c.6 0 1 .6.8 1.2L9 9.3c-.1.4-.5.7-.9.7H3z" fill="#fff"/></svg>30 Tage Geld-Zurück-Garantie</span>
  <span style="left:893px"><svg width="10" height="10" viewBox="0 0 10 10"><path d="M2 0l2 2.5-1.2 1.3c.7 1.4 1.8 2.5 3.3 3.3L7.4 6 10 8 8.6 9.8C4.5 10 0 5.5.2 1.4z" fill="#fff"/></svg>24h Hotline 0421 - 58 21 947</span>
</div>

<section class="hero">
  <div class="hero-visual" role="img" aria-label="Zwei dunkle Teelichterkerzen in Gläsern mit Silberdekor auf einem versilberten Tablett"></div>
  <h1 class="hero-title main">Die Teelichterkerze</h1>
  <h2 class="hero-title sub">Entdecke die genial Idee</h2>
  <div class="hero-cta" style="left:221px"><span class="label">KERZE MIT Ø 8CM</span><span class="arrow"><svg width="22" height="10" viewBox="0 0 22 10"><path d="M0 5h20M16 1l4 4-4 4" fill="none" stroke="#fff" stroke-width="1.2"/></svg></span></div>
  <div class="hero-cta" style="left:451px"><span class="label">KERZE MIT Ø 10CM</span><span class="arrow"><svg width="22" height="10" viewBox="0 0 22 10"><path d="M0 5h20M16 1l4 4-4 4" fill="none" stroke="#fff" stroke-width="1.2"/></svg></span></div>
</section>

<div class="tile" style="left:161px;background:linear-gradient(160deg,#c9c2b4,#a9a08c 60%,#c8b68a)" role="img" aria-label="Bar-Zubehör mit Flaschen und versilbertem Becher"></div>
<div class="tile" style="left:384px;background:linear-gradient(160deg,#e8e8ea,#d4c9b6 55%,#c7a16a)" role="img" aria-label="Frühstückstisch mit versilbertem Eierbecher"></div>
<div class="tile" style="left:607px;background:linear-gradient(160deg,#ece6d8,#c9c3a4 55%,#b6b193)" role="img" aria-label="Wohnzimmer-Deko mit Blumen und Bilderrahmen"></div>
<div class="tile" style="left:829px;background:linear-gradient(160deg,#eef0f2,#d7dadd 55%,#c5c8cc)" role="img" aria-label="Helles Wohnzimmer mit Bilderrahmen an der Wand"></div>
</body>
</html>
```